Paramount Vigor Product design

We need a bottle design for our product. Paramount Vigor is a Gaming Nootropic made to increase Energy, Focus, Reaction time, and Clarity of an eSport gamer. It will be 40 servings a bottle. Currently, all the ingredients haven't been finalized so after the competition is over we will have to work with the designer to also make an ingredients label for the back of it. For the flavor, we will call it tundra mist.

The attachments included:. The velvet lanterns picture as a font style I like for the logo.
The Z BOOST QUENCH PICTURE IS WHAT WE WANT OUR DESIGN to look like something similar a clean and simple design that stands out!

Z Boost bottle is what our biggest competitors product looks like. The paramount vigor picture as the current logo we are using but can be changed.

Overall the pictures are just some references for what I could possibly want the design to look like however, I'm open to your designer's ideas and concepts you think would make for a cool looking Gaming Nootropic product bottle design. I appreciate everyone working on this and look forward to seeing your designs have a great day!

Target Market(s)

Gamers between the ages of 18-30

Industry/Entity Type

Health And Wellness

Requirements
Must have
• Paramount Vigor logo, state that it is for energy, focus, reaction, and clarity. state 40 serivngs. state flavor.

```html
<!DOCTYPE html>
<html lang="en">
<head>
<meta charset="utf-8">
<title>Paramount Vigor – Tundra Mist Label</title>
<link rel="stylesheet" href="https://fonts.googleapis.com/css2?family=Roboto+Condensed:ital,wght@0,700;1,500&display=swap">
<style>
  :root {
    --page: #f7f7f7;
    --sky-edge: #93b8dc;
    --sky-mid: #c6dbef;
    --glow: #ffffff;
    --brand-blue: #1767ae;
    --band-blue: #1565a9;
    --title-blue: #1a6cb6;
    --white: #ffffff;
  }
  * { box-sizing: border-box; margin: 0; padding: 0; }
  html, body { width: 1200px; height: 1200px; overflow: hidden; background: var(--page); }
  body { position: relative; font-family: "Roboto Condensed", "Arial Narrow", sans-serif; }

  .label {
    position: absolute; left: 70px; top: 451px; width: 1060px; height: 299px;
    overflow: hidden;
    background:
      radial-gradient(ellipse 60% 22% at 50% 36%, var(--glow) 0%, rgba(255,255,255,0.6) 45%, rgba(255,255,255,0) 100%),
      linear-gradient(90deg, var(--sky-edge) 0%, var(--sky-mid) 35%, #e8f1fa 50%, var(--sky-mid) 65%, var(--sky-edge) 100%);
  }
  .texture-band {
    position: absolute; left: 0; top: 0; width: 100%; height: 70px;
    background: linear-gradient(90deg, rgba(90,150,210,0.35) 0%, rgba(255,255,255,0) 45%, rgba(255,255,255,0) 55%, rgba(90,150,210,0.35) 100%);
  }
  .servings-badge {
    position: absolute; left: 604px; top: 0; width: 65px; height: 81px;
    background: var(--brand-blue); border-radius: 0 0 5px 5px;
    color: var(--white); text-align: center;
  }
  .servings-count { display: block; font-weight: 700; font-size: 34px; line-height: 1; margin-top: 12px; }
  .servings-word { display: block; font-style: italic; font-weight: 500; font-size: 13px; margin-top: 1px; }

  .brand-dot {
    position: absolute; left: 500px; top: 72px; width: 60px; height: 60px;
    border-radius: 50%; background: var(--brand-blue);
  }
  .flavor-name {
    position: absolute; left: 0; width: 100%; top: 146px;
    text-align: center; color: var(--title-blue);
    font-weight: 700; font-size: 42px; letter-spacing: 0.5px; line-height: 1;
  }
  .benefit-tab {
    position: absolute; left: 393px; top: 208px; width: 276px; height: 36px;
    background: var(--brand-blue); border-radius: 5px 5px 0 0;
    color: var(--white); font-style: italic; font-weight: 500; font-size: 19px;
    text-align: center; line-height: 32px;
  }
  .base-band {
    position: absolute; left: 0; top: 235px; width: 100%; height: 64px;
    background: var(--band-blue);
  }
  .brand-lockup {
    position: absolute; left: 47px; top: 250px; display: flex; align-items: center; gap: 8px;
    color: var(--white); font-weight: 700; font-size: 12.5px; letter-spacing: 0.2px;
  }
  .brand-lockup .mark-dot { width: 22px; height: 22px; border-radius: 50%; background: var(--white); }
  .mountain-art {
    position: absolute; left: 404px; top: 251px; width: 258px; height: 48px;
    background: linear-gradient(180deg, rgba(255,255,255,0.95) 0%, rgba(225,238,250,0.9) 100%);
    border-radius: 40% 50% 0 0 / 100% 100% 0 0;
  }
</style>
</head>
<body>
  <main class="label">
    <div class="texture-band" role="img" aria-label="Soft blue halftone dot texture"></div>
    <div class="servings-badge">
      <span class="servings-count">40</span>
      <span class="servings-word">serivngs</span>
    </div>
    <div class="brand-dot" aria-hidden="true"></div>
    <h1 class="flavor-name">TUNDRA MIST</h1>
    <div class="base-band"></div>
    <div class="benefit-tab">energy • focus • reaction • clarity</div>
    <div class="brand-lockup"><span class="mark-dot"></span><span>PARAMOUNT VIGOR</span></div>
    <div class="mountain-art" role="img" aria-label="White snowy mountain peak illustration"></div>
  </main>
</body>
</html>
```